依頼詳細
折込日
10/27(金)山梨県内32万部 新聞折込チラシ B4両面カラー 紙質は要相談
見学会日程
10/27~29(金~日)計3日間  10:00~17:00

二会場同時 秋の現場見学会(甲府市・甲斐市)
記載項目
東峰ホーム株式会社/秋の現場見学会/公式HP http://www.tohohome-example.jp/
HP内のチラシ掲載ページを参照ください。
補足内容が必要な場合は
sawada@tohohome-example.jp
又は0559876543(担当:沢田)まで
ご連絡をお願い致します。
サイズ
B4
ページ数
両面
希望イメージ
シンプル 複雑
単色 カラフル
暗い 明るい
日常 高級
遊び心 厳粛
未来的 伝統的
女性的 男性的
希望する色
水色系
納品ファイル
• イラストレーター形式 (.ai)
分譲地二か所の詳細データ
甲斐市龍地新規分譲
http://25.filebox-example.jp/1014-a1b2c3d4e5f60718293a4b5c6d7e8f90

甲府市上今井町新規分譲
http://13.filebox-example.jp/1014-0f9e8d7c6b5a49382716a5b4c3d2e1f0
■■■制作原稿のサイズ変更■■■

新聞折込チラシB4サイズから、新聞広告全15段へ変更になりました。
申し訳ありませんが、ご対応をお願い致します。

掲載用データ作成の案内を添付いたしましたので
ご確認後に制作をお願い致します。
選考は明日の午後3時頃までに行います。
色々なご提案頂きありがとうございました。

別件で、ロゴマークの制作の発注も行いますので
各ランサー様にご提案頂ければと思います。

今後とも宜しくお願い致します。

問合せにつながる内容を重視致しました。

様々なご提案頂き誠にありがとうございました。
選考にお時間がかかってしまい申し訳ありません。
今後も定期的に依頼を予定しておりますので、
引き続きよろしくお願い致します。

企画・広報担当:沢田

```html
<!DOCTYPE html>
<html lang="ja">
<head>
<meta charset="utf-8">
<title>秋の現場見学会</title>
<link href="https://fonts.googleapis.com/css2?family=Noto+Sans+JP:wght@400;700;900&family=Noto+Serif+JP:wght@700;900&display=swap" rel="stylesheet">
<style>
:root{
  --blue:#1c7fc4;
  --sky:#4fb3e6;
  --pale:#e8f5fc;
  --red:#d7261e;
  --green:#3a9a3a;
  --ink:#222;
  --grey:#8a96a0;
  --photo:#9fb2a3;
  --autumn:#e8a24a;
}
*{margin:0;padding:0;box-sizing:border-box}
html,body{width:885px;height:1200px;overflow:hidden;background:#fff}
body{font-family:"Noto Sans JP",sans-serif;color:var(--ink);position:relative}
.abs{position:absolute}
.area-label{background:var(--blue);color:#fff;width:220px;padding:8px 12px}
.area-label .city{font-size:22px;font-weight:700;line-height:1.1}
.area-label .town{font-size:50px;font-weight:900;line-height:1}
.area-label .roman{font-size:10px;font-style:normal;display:block}
.area-label .type{font-size:22px;font-weight:700}
.price{color:var(--blue);font-family:"Noto Serif JP",serif;font-weight:900;font-size:44px;line-height:1.05}
.price small{font-size:24px}
.spec{font-size:12px;line-height:1.5;color:#333}
.catch{background:var(--sky);color:#fff;font-weight:700;font-size:18px;line-height:1.5;padding:10px 16px;border-radius:6px;white-space:nowrap}
.ph{background:linear-gradient(160deg,#b9d4e6,var(--photo) 60%,#b8a98a)}
.siteplan{background:linear-gradient(135deg,#f3f6f3,#dfe7e2)}
.map{background:#f0f0ee;border:1px solid #ccc;display:flex;align-items:center;justify-content:center;font-size:18px;font-weight:700;color:#999}
.badge{width:70px;height:70px;border-radius:50%;background:var(--green);color:#fff;display:flex;flex-direction:column;align-items:center;justify-content:center;font-weight:700;font-size:13px;line-height:1.1}
.badge b{font-size:22px}
.caption{font-size:9.5px;color:#444;background:#eef4f8;padding:3px 8px;white-space:nowrap}
.tag{background:var(--blue);color:#fff;font-size:11px;padding:2px 6px}
.event{left:0;top:410px;width:885px;height:255px;background:linear-gradient(180deg,#fff 0%,#fff6ea 100%)}
.leaves{background:linear-gradient(120deg,#f2c27a,var(--autumn) 60%,#c9562c)}
.twin{background:var(--red);color:#fff;font-weight:900;font-size:30px;line-height:1.2;padding:10px 8px;text-align:center;width:116px;white-space:nowrap}
.dates{font-weight:900;font-size:46px;color:var(--ink);font-family:"Noto Sans JP",sans-serif;white-space:nowrap}
.dates .d{font-size:20px;background:var(--ink);color:#fff;border-radius:50%;display:inline-block;width:30px;height:30px;text-align:center;line-height:30px;vertical-align:middle;margin:0 2px}
.dates .sat{background:var(--blue)}.dates .sun{background:var(--red)}
.time{font-size:20px;font-weight:700;line-height:1.15}
.title{font-family:"Noto Serif JP",serif;font-weight:900;font-size:86px;color:var(--ink);letter-spacing:2px;white-space:nowrap}
.title .aki{color:var(--red);font-size:118px}
.footer{left:0;top:1136px;width:885px;height:64px;border-top:3px solid var(--blue);display:flex;align-items:center;padding:0 18px;gap:16px}
.brand{font-weight:700;font-size:22px;color:var(--blue);display:flex;align-items:center;gap:8px;white-space:nowrap}
.brand i{width:18px;height:18px;background:var(--red);display:inline-block}
.tel{font-weight:900;font-size:30px;color:var(--blue);display:flex;align-items:center;gap:6px;white-space:nowrap}
.fine{font-size:10px;line-height:1.4;color:#333}
</style>
</head>
<body>

<section>
  <div class="abs area-label" style="left:12px;top:12px">
    <div class="city">甲斐市</div>
    <div class="town">龍地</div>
    <em class="roman">kaishi Ryuji</em>
    <div class="type">新規分譲</div>
  </div>
  <div class="abs price" style="left:14px;top:220px">731<small>万円~</small><br>897<small>万円</small></div>
  <div class="abs spec" style="left:14px;top:330px">区画面積<br>201.43m²(60.93坪)〜<br>224.77m²(67.99坪)</div>

  <div class="abs catch" style="left:250px;top:12px;width:360px">生活圏に商業施設が多数ありながらも、<br>ゆったりとした生活ができる立地。</div>
  <div class="abs ph" role="img" aria-label="龍地分譲地の造成済み区画写真" style="left:250px;top:105px;width:360px;height:150px"></div>
  <div class="abs ph" role="img" aria-label="周辺の商業施設写真" style="left:250px;top:262px;width:118px;height:80px"></div>
  <div class="abs ph" role="img" aria-label="周辺の街並み写真" style="left:371px;top:262px;width:118px;height:80px"></div>
  <div class="abs ph" role="img" aria-label="周辺環境写真" style="left:492px;top:262px;width:118px;height:80px"></div>
  <div class="abs tag" style="left:380px;top:265px">周辺環境</div>
  <div class="abs caption" style="left:250px;top:348px;width:360px">車両距離：JR中央線「竜王駅」車で約5分／スーパー・病院・学校が徒歩圏内</div>

  <div class="abs siteplan" role="img" aria-label="龍地分譲地の区画図" style="left:620px;top:12px;width:255px;height:190px"></div>
  <div class="abs badge" style="left:800px;top:180px">全<b>34</b>区画</div>
  <div class="abs map" role="img" aria-label="龍地分譲地の案内地図" style="left:620px;top:260px;width:255px;height:140px">MAP</div>
</section>

<section class="abs event">
  <div class="abs leaves" role="img" aria-label="紅葉の装飾" style="left:0;top:0;width:885px;height:22px"></div>
  <div class="abs dates" style="left:260px;top:32px">10/27<span class="d">金</span>・28<span class="d sat">土</span>・29<span class="d sun">日</span></div>
  <div class="abs time" style="left:770px;top:42px">10:00〜<br>17:00</div>
  <div class="abs twin" style="left:24px;top:104px">二会場<br>同時</div>
  <div class="abs title" style="left:158px;top:80px"><span class="aki">秋</span>の現場見学会</div>
  <div class="abs leaves" role="img" aria-label="紅葉の装飾" style="left:0;top:233px;width:885px;height:22px"></div>
</section>

<section>
  <div class="abs area-label" style="left:12px;top:680px">
    <div class="city">甲斐市</div>
    <div class="town" style="font-size:40px">上今井町</div>
    <em class="roman">kaishi Kamiimai</em>
    <div class="type">新規分譲</div>
  </div>
  <div class="abs price" style="left:14px;top:890px">734<small>万円~</small><br>1,174<small>万円</small></div>
  <div class="abs spec" style="left:14px;top:1000px">区画面積<br>200.00m²(60.50坪)〜<br>323.20m²(97.77坪)</div>

  <div class="abs catch" style="left:250px;top:680px;width:360px">生活圏に商業施設が多数ありながらも、<br>ゆったりとした生活ができる立地。</div>
  <div class="abs ph" role="img" aria-label="上今井町分譲地の空撮写真" style="left:250px;top:773px;width:360px;height:170px"></div>
  <div class="abs ph" role="img" aria-label="周辺の商業施設写真" style="left:250px;top:950px;width:118px;height:80px"></div>
  <div class="abs ph" role="img" aria-label="周辺の街並み写真" style="left:371px;top:950px;width:118px;height:80px"></div>
  <div class="abs ph" role="img" aria-label="周辺環境写真" style="left:492px;top:950px;width:118px;height:80px"></div>
  <div class="abs tag" style="left:380px;top:953px">周辺環境</div>
  <div class="abs caption" style="left:250px;top:1036px;width:360px">車両距離：JR中央線「竜王駅」車で約8分／スーパー・病院・学校が徒歩圏内</div>

  <div class="abs siteplan" role="img" aria-label="上今井町分譲地の区画図" style="left:620px;top:680px;width:255px;height:190px"></div>
  <div class="abs badge" style="left:800px;top:690px">全<b>47</b>区画</div>
  <div class="abs map" role="img" aria-label="上今井町分譲地の案内地図" style="left:620px;top:930px;width:255px;height:190px">MAP</div>
</section>

<footer class="abs footer">
  <div class="fine">売主・施工<br>一級建築士事務所</div>
  <div class="brand"><i></i>東峰ホーム株式会社</div>
  <div class="tel">
    <svg width="30" height="24" viewBox="0 0 30 24"><rect x="1" y="2" width="28" height="20" rx="4" fill="#1c7fc4"/><text x="15" y="17" font-size="12" font-weight="700" fill="#fff" text-anchor="middle" font-family="Noto Sans JP,sans-serif">通話</text></svg>
    0120-555-018
  </div>
  <div class="fine">〒400-0000 山梨県甲府市中央1-2-3<br>営業時間 9:00〜18:00<br>http://www.tohohome-example.jp/</div>
</footer>

</body>
</html>
```